Book Cover "Venice"

Creation of a cover (14 x 20.5 cm + bleed area) for a book:
Image: “BrumeVerte” (Tiff joined)
AUTHOR: Maribel Quonte
TITLE: The murmurs of Oldmere
PUBLISHER: Editions Plavoc (AT THE BOTTOM OF THE COVER)
Updates

Target Market(s)

Readers of romantic novels

Industry/Entity Type

Book

```html
<!DOCTYPE html>
<html lang="en">
<head>
<meta charset="utf-8">
<title>The Murmurs of Oldmere — Maribel Quonte</title>
<link rel="stylesheet" href="https://fonts.googleapis.com/css2?family=Poppins:wght@300;400&family=Playfair+Display:wght@400&display=swap">
<style>
  :root {
    --sky-top: #4a0c12;
    --sky-upper: #9a1318;
    --sky-mid: #d5121a;
    --sky-low: #e2301c;
    --dusk: #b3241c;
    --silhouette: #1a0d1c;
    --author: #e8521f;
    --title: #ffffff;
    --publisher: #e2dcdc;
  }
  html, body {
    margin: 0;
    padding: 0;
    width: 820px;
    height: 1200px;
    overflow: hidden;
    background: var(--sky-top);
  }
  .cover {
    position: relative;
    width: 820px;
    height: 1200px;
    overflow: hidden;
  }
  .cover-photo {
    position: absolute;
    inset: 0;
    background: linear-gradient(180deg,
      var(--sky-top) 0%,
      var(--sky-upper) 12%,
      var(--sky-mid) 35%,
      var(--sky-low) 58%,
      var(--dusk) 72%,
      var(--silhouette) 86%,
      var(--silhouette) 100%);
  }
  .author {
    position: absolute;
    top: 42px;
    left: 0;
    width: 100%;
    text-align: center;
    font-family: "Poppins", sans-serif;
    font-weight: 300;
    font-size: 66px;
    letter-spacing: 5px;
    color: var(--author);
    margin: 0;
    text-transform: uppercase;
    text-shadow: 0 2px 4px rgba(0,0,0,0.25);
  }
  .title {
    position: absolute;
    top: 262px;
    left: 0;
    width: 100%;
    margin: 0;
    text-align: center;
    font-family: "Playfair Display", serif;
    font-weight: 400;
    color: var(--title);
    text-shadow: 0 2px 5px rgba(0,0,0,0.25);
  }
  .title span { display: block; }
  .title .small-word {
    font-size: 66px;
    line-height: 70px;
  }
  .title .main-word {
    font-size: 112px;
    line-height: 118px;
    letter-spacing: -2px;
  }
  .title .line-the { margin-left: 60px; }
  .title .line-of { margin-left: 40px; }
  .publisher {
    position: absolute;
    bottom: 18px;
    left: 0;
    width: 100%;
    text-align: center;
    font-family: "Poppins", sans-serif;
    font-weight: 400;
    font-size: 24px;
    color: var(--publisher);
    margin: 0;
  }
</style>
</head>
<body>
  <main class="cover">
    <div class="cover-photo" role="img" aria-label="Photograph of a blazing red sunset sky over the silhouetted domes and bell towers of a lagoon city, with lit street lanterns in the foreground"></div>
    <p class="author">Maribel Quonte</p>
    <h1 class="title">
      <span class="small-word line-the">The</span>
      <span class="main-word">Murmurs</span>
      <span class="small-word line-of">of</span>
      <span class="main-word">Oldmere</span>
    </h1>
    <p class="publisher">Editions Plavoc</p>
  </main>
</body>
</html>
```